Zielgruppe
Beratung und Live-Kommunikation
Aufgabenstellung
- Re-Design vom Firmenlogo und Briefpapier
- Anpassung/ Abwandlung der vorhandenen Elemente (Briefkopf). Anordnung, Schrift, etc.
- Ideen, wie man den Inhalt (den Tätigkeitsbereich) ggfs. grafisch ansprechend als Logo darstellen kann.
- Klare Linien, symmetrisch. Schwarz-weiß/keine Farbe
- Briefpapier auf *.doc Basis, kein randloser Druck
- derzeitiger Stil siehe www.stagewerk-buero.de

```html
<!DOCTYPE html>
<html lang="de">
<head>
<meta charset="utf-8">
<title>Briefpapier – brettmeier stagewerk büro</title>
<link rel="stylesheet" href="https://fonts.googleapis.com/css2?family=Questrial&display=swap">
<style>
:root{
  --paper:#ffffff;
  --ink:#000000;
  --text:#1e1e1e;
  --mark:#555555;
}
*{margin:0;padding:0;box-sizing:border-box}
html,body{width:858px;height:1200px;overflow:hidden;background:var(--paper)}
.sheet{position:relative;width:858px;height:1200px;background:var(--paper);font-family:"Questrial",sans-serif;color:var(--text)}
.brand{position:absolute;right:39px;top:64px;text-align:right;color:var(--ink);font-family:"Questrial",sans-serif;font-weight:400}
.brand-name{display:flex;align-items:center;justify-content:flex-end;font-size:22px;line-height:26px;letter-spacing:3px;white-space:nowrap}
.brand-square{width:14px;height:14px;background:var(--ink);margin-right:10px;flex:none}
.brand-sub{font-size:22px;line-height:26px;letter-spacing:3px;white-space:nowrap}
.services{position:absolute;right:39px;top:132px;text-align:right;color:var(--ink);font-size:16px;line-height:25px;letter-spacing:2.4px;list-style:none}
.window-mark{position:absolute;width:9px;height:9px;border-color:var(--mark);border-style:solid;border-width:0}
.wm-tl{left:97px;top:183px;border-top-width:1px;border-left-width:1px}
.wm-tr{left:435px;top:183px;border-top-width:1px;border-right-width:1px}
.wm-bl{left:97px;top:359px;border-bottom-width:1px;border-left-width:1px}
.wm-br{left:435px;top:359px;border-bottom-width:1px;border-right-width:1px}
.sender-line{position:absolute;left:117px;top:190px;font-size:11.4px;color:var(--ink);white-space:nowrap}
.fold-mark{position:absolute;width:11px;height:0;border-top:1px solid var(--mark)}
.fold-left-1{left:0;top:429px}
.fold-right-1{right:0;top:429px}
.fold-left-2{left:0;top:857px}
.contact{position:absolute;left:595px;width:255px;font-size:11.2px;line-height:14px}
.contact-item{display:flex;align-items:flex-start;margin-bottom:8px}
.contact-item .icon{width:17px;height:17px;flex:none;margin-right:10px;margin-top:-1px}
.company{font-weight:700;color:var(--ink)}
.contact-header{top:264px}
.contact-footer{top:847px}
.bank{margin-top:18px}
.legal{margin-top:24px}
.legal .court{margin-top:14px}
.payment-note{position:absolute;left:97px;top:1090px;width:468px;font-size:11px;line-height:14px;color:var(--text)}
</style>
</head>
<body>
<main class="sheet">
  <header>
    <div class="brand">
      <p class="brand-name"><span class="brand-square"></span>JONAS BRETTMEIER</p>
      <p class="brand-sub">STAGEWERKBUERO</p>
    </div>
    <ul class="services">
      <li>BERATUNG</li>
      <li>PLANUNG</li>
      <li>UMSETZUNG</li>
    </ul>
  </header>

  <section class="address-window">
    <span class="window-mark wm-tl"></span><span class="window-mark wm-tr"></span>
    <span class="window-mark wm-bl"></span><span class="window-mark wm-br"></span>
    <p class="sender-line">Brettmeier&nbsp; |&nbsp; Lindenweg 4b&nbsp; |&nbsp; D-42853 Remscheid</p>
  </section>

  <span class="fold-mark fold-left-1"></span>
  <span class="fold-mark fold-right-1"></span>
  <span class="fold-mark fold-left-2"></span>

  <section class="contact contact-header">
    <div class="contact-item">
      <svg class="icon" viewBox="0 0 17 17" aria-hidden="true"><rect width="17" height="17" fill="#000"/><path d="M8.5 3a3.5 3.5 0 0 0-3.5 3.5c0 2.6 3.5 6.5 3.5 6.5s3.5-3.9 3.5-6.5A3.5 3.5 0 0 0 8.5 3z" fill="none" stroke="#fff" stroke-width="1.2"/></svg>
      <div><span class="company">brettmeier stagewerk büro GmbH</span><br>Lindenweg 4b<br>D-42853 Remscheid</div>
    </div>
    <div class="contact-item">
      <svg class="icon" viewBox="0 0 17 17" aria-hidden="true"><rect width="17" height="17" fill="#000"/><circle cx="8.5" cy="8.5" r="5" fill="none" stroke="#fff" stroke-width=".8"/><ellipse cx="8.5" cy="8.5" rx="2.2" ry="5" fill="none" stroke="#fff" stroke-width=".8"/><path d="M3.5 8.5h10" stroke="#fff" stroke-width=".8"/></svg>
      <div>stagewerk-buero.gmbh</div>
    </div>
    <div class="contact-item">
      <svg class="icon" viewBox="0 0 17 17" aria-hidden="true"><rect width="17" height="17" fill="#000"/><path d="M5 3.5l2 2.5-1.2 1.3c.7 1.5 1.9 2.7 3.4 3.4L10.5 9.5 13 11.5l-1.4 1.9C7.5 13 4 9.5 3.6 5z" fill="#fff"/></svg>
      <div>+49 (0)151 000 123 45</div>
    </div>
    <div class="contact-item">
      <svg class="icon" viewBox="0 0 17 17" aria-hidden="true"><rect width="17" height="17" fill="#000"/><rect x="3.5" y="5" width="10" height="7" fill="none" stroke="#fff" stroke-width=".9"/><path d="M3.5 5l5 4 5-4" fill="none" stroke="#fff" stroke-width=".9"/></svg>
      <div>brettmeier@stagewerk-buero.gmbh</div>
    </div>
    <div class="contact-item">
      <svg class="icon" viewBox="0 0 17 17" aria-hidden="true"><rect width="17" height="17" fill="#000"/></svg>
      <div>brett_stagewerk</div>
    </div>
  </section>

  <section class="contact contact-footer">
    <div class="contact-item">
      <svg class="icon" viewBox="0 0 17 17" aria-hidden="true"><rect width="17" height="17" fill="#000"/><path d="M8.5 3a3.5 3.5 0 0 0-3.5 3.5c0 2.6 3.5 6.5 3.5 6.5s3.5-3.9 3.5-6.5A3.5 3.5 0 0 0 8.5 3z" fill="none" stroke="#fff" stroke-width="1.2"/></svg>
      <div><span class="company">brettmeier stagewerk büro GmbH</span><br>Lindenweg 4b<br>D-42853 Remscheid</div>
    </div>
    <div class="contact-item">
      <svg class="icon" viewBox="0 0 17 17" aria-hidden="true"><rect width="17" height="17" fill="#000"/><circle cx="8.5" cy="8.5" r="5" fill="none" stroke="#fff" stroke-width=".8"/><ellipse cx="8.5" cy="8.5" rx="2.2" ry="5" fill="none" stroke="#fff" stroke-width=".8"/><path d="M3.5 8.5h10" stroke="#fff" stroke-width=".8"/></svg>
      <div>stagewerk-buero.gmbh</div>
    </div>
    <div class="contact-item">
      <svg class="icon" viewBox="0 0 17 17" aria-hidden="true"><rect width="17" height="17" fill="#000"/><path d="M5 3.5l2 2.5-1.2 1.3c.7 1.5 1.9 2.7 3.4 3.4L10.5 9.5 13 11.5l-1.4 1.9C7.5 13 4 9.5 3.6 5z" fill="#fff"/></svg>
      <div>+49 (0)151 000 123 45</div>
    </div>
    <div class="contact-item">
      <svg class="icon" viewBox="0 0 17 17" aria-hidden="true"><rect width="17" height="17" fill="#000"/><rect x="3.5" y="5" width="10" height="7" fill="none" stroke="#fff" stroke-width=".9"/><path d="M3.5 5l5 4 5-4" fill="none" stroke="#fff" stroke-width=".9"/></svg>
      <div>brettmeier@stagewerk-buero.gmbh</div>
    </div>
    <div class="contact-item">
      <svg class="icon" viewBox="0 0 17 17" aria-hidden="true"><rect width="17" height="17" fill="#000"/></svg>
      <div>brett_stagewerk</div>
    </div>

    <div class="contact-item bank">
      <svg class="icon" viewBox="0 0 17 17" aria-hidden="true"><rect width="17" height="17" fill="#000"/><path d="M3 6.5L8.5 3.5 14 6.5z" fill="#fff"/><rect x="4" y="7.5" width="1.5" height="5" fill="#fff"/><rect x="7.75" y="7.5" width="1.5" height="5" fill="#fff"/><rect x="11.5" y="7.5" width="1.5" height="5" fill="#fff"/><rect x="3" y="13" width="11" height="1.2" fill="#fff"/></svg>
      <div>Volksbank Bergland Nord<br>IBAN DE00.1234.5678.9012.3456.78<br>BIC GENODEX1BGN</div>
    </div>

    <div class="contact-item legal">
      <svg class="icon" viewBox="0 0 17 17" aria-hidden="true"><rect width="17" height="17" fill="#000"/><rect x="3.5" y="3" width="7.5" height="10" fill="none" stroke="#fff" stroke-width=".9"/><path d="M5 5.5h4.5M5 7.5h3" stroke="#fff" stroke-width=".8"/><circle cx="11" cy="11" r="2" fill="#000" stroke="#fff" stroke-width=".9"/><path d="M12.4 12.4l1.6 1.6" stroke="#fff" stroke-width="1"/></svg>
      <div>Jonas Brettmeier<br>Finanzamt Remscheid<br>Steuer-Nr. 000.1234.5678<br>USt-IdNr. DE000.123.456<p class="court">Amtsgericht Wuppertal HRB 00000</p></div>
    </div>
  </section>

  <footer class="payment-note">
    Endbetrag zahlbar sofort nach Erhalt innerhalb von 10 Tagen ohne Abzug auf das genannte Konto. Die Leistung ist bereits erbracht. Der Betrag wird beim Finanzamt Remscheid ordnungsgemäß versteuert. Eine erweiterte Aufschlüsselung der Summen und Belegkopien befinden sich ggfs. in der Anlage. Auslagen und Verpflegungsmehraufwendungen können separat in Rechnung gestellt werden.
  </footer>
</main>
</body>
</html>
```